Velmoran advertisement one page flyer design

We need a flyer design for our company to advertise what we offer, it only needs to be one sided, approx A5 in size.
Our logo: http://velmoran-example.com/images/logo.png (I will provide in high-res later)
We offer, website design, development, bespoke applications. We would like to advertise that we can be hired for short term contracts for companies who need help with their work load.
Some of, but not limited to the systems we build are content management systems, e-commerce systems & event booking systems.
Our strap line is "We design, develop and deliver", a nice sleek redesign of the image on our website would be nice, but not required 100% - http://velmoran-example.com/
Other details to put on the flyer:-
Email: hello@velmoran-example.com
Tel: 01632 960 471
Address: Velmoran Ltd, Brisk Suites, Quenby Road, Cheltenham, GL53 9TQ
We welcome any other ideas.

```html
<!DOCTYPE html>
<html lang="en">
<head>
<meta charset="utf-8">
<title>Velmoran Flyer</title>
<link rel="stylesheet" href="https://fonts.googleapis.com/css2?family=Cabin:wght@600;700&family=Comic+Neue:wght@700&family=Arimo:wght@400;700&family=Chakra+Petch:wght@700&display=swap">
<style>
  :root {
    --backdrop: #3b2216;
    --orange: #e6791c;
    --orange-deep: #b5400c;
    --orange-dark: #8a2a08;
    --grey-band: #858585;
    --ink: #2b2b2b;
    --wordmark-grey: #4a4a4a;
    --brand-grey: #d9d9d9;
    --white: #ffffff;
  }
  * { margin: 0; padding: 0; box-sizing: border-box; }
  html, body { width: 891px; height: 1200px; overflow: hidden; }
  body { background: var(--backdrop); position: relative; font-family: "Arimo", Arial, sans-serif; }

  .flyer { position: absolute; left: 57px; top: 47px; width: 778px; height: 1106px; background: var(--white); overflow: hidden; }

  .hero { position: absolute; left: 0; top: 0; width: 778px; height: 338px;
    background: linear-gradient(100deg, var(--orange-dark) 0%, var(--orange-deep) 35%, #d8661a 70%, #e88a2a 100%); }
  .hero-visual { position: absolute; right: 0; top: 0; width: 380px; height: 338px;
    background: radial-gradient(ellipse at 60% 35%, rgba(255,205,120,0.75) 0%, rgba(240,150,50,0.45) 40%, rgba(200,90,20,0) 75%); }
  .brand-name { position: absolute; left: 32px; top: 38px; font-family: "Cabin", sans-serif; font-weight: 700; font-size: 66px; line-height: 1; color: var(--brand-grey); letter-spacing: 1px; }
  .hero-copy { position: absolute; left: 30px; top: 158px; font-family: "Cabin", sans-serif; font-weight: 700; font-size: 20px; line-height: 27.5px; color: var(--white); letter-spacing: 1.9px; }
  .hero-copy p + p { margin-top: 27.5px; }

  .process { position: absolute; left: 0; top: 338px; width: 778px; height: 347px; background: var(--grey-band); }
  .section-title { font-family: "Comic Neue", "Comic Sans MS", cursive; font-weight: 700; color: var(--ink); text-align: center; position: absolute; left: 0; width: 100%; letter-spacing: 2px; line-height: 1.2; }
  .process .section-title { top: 36px; font-size: 46px; }
  .steps { position: absolute; top: 123px; left: 0; width: 100%; }
  .step { position: absolute; top: 0; width: 220px; margin-left: -110px; text-align: center; }
  .step-badge { width: 106px; height: 106px; margin: 0 auto; background: var(--orange);
    border-radius: 50% 0 50% 50%; display: flex; align-items: center; justify-content: center; }
  .step-badge svg { width: 66px; height: 66px; }
  .step-word { font-family: "Chakra Petch", sans-serif; font-weight: 700; font-size: 64px; line-height: 1; color: var(--wordmark-grey); margin-top: 10px; letter-spacing: -1px; }

  .solutions { position: absolute; left: 0; top: 685px; width: 778px; height: 341px; background: var(--orange); }
  .solutions .section-title { top: 28px; font-size: 48px; }
  .solution { position: absolute; width: 260px; margin-left: -130px; text-align: center; }
  .solution svg { width: 46px; height: 46px; display: block; margin: 0 auto 8px; }
  .solution-label { font-weight: 700; font-size: 18.5px; color: var(--white); }

  .contact { position: absolute; left: 0; top: 1026px; width: 778px; height: 80px; background: var(--white); color: #111; text-align: center; }
  .contact-line { display: flex; justify-content: center; align-items: center; gap: 10px; }
  .contact-line.primary { font-size: 25px; margin-top: 9px; }
  .contact-line.address { font-size: 19px; margin-top: 6px; }
  .contact-line svg { flex: none; }
  .gap { width: 20px; }
</style>
</head>
<body>
<main class="flyer">
  <header class="hero">
    <div class="hero-visual" role="img" aria-label="Glowing orange web interface tiles with a hand pointing at one of them"></div>
    <div class="brand-name">Velmoran</div>
    <div class="hero-copy">
      <p>We offer, website design,<br>development, bespoke application</p>
      <p>we can be hired for short term contract<br>for. companies who need help with<br>then work load</p>
    </div>
  </header>

  <section class="process">
    <h2 class="section-title">How It Works?</h2>
    <div class="steps">
      <div class="step" style="left:126px">
        <div class="step-badge">
          <svg viewBox="0 0 64 64" fill="#fff"><rect x="28" y="4" width="9" height="46" rx="2" transform="rotate(-40 32 32)"/><rect x="28" y="8" width="7" height="44" rx="3" transform="rotate(40 32 32)"/></svg>
        </div>
        <div class="step-word">design</div>
      </div>
      <div class="step" style="left:385px">
        <div class="step-badge">
          <svg viewBox="0 0 64 64" fill="#fff"><rect x="28" y="4" width="8" height="56" rx="3" transform="rotate(45 32 32)"/><rect x="28" y="14" width="8" height="46" rx="3" transform="rotate(-45 32 32)"/><circle cx="15" cy="15" r="9"/></svg>
        </div>
        <div class="step-word">devlop</div>
      </div>
      <div class="step" style="left:643px">
        <div class="step-badge">
          <svg viewBox="0 0 64 64" fill="#fff"><path d="M14 6h6l8 40h26v5H24z"/><circle cx="26" cy="54" r="5"/><rect x="30" y="28" width="20" height="15" transform="rotate(-12 40 36)"/><rect x="34" y="12" width="14" height="13" transform="rotate(-12 41 18)"/></svg>
        </div>
        <div class="step-word">deliver</div>
      </div>
    </div>
  </section>

  <section class="solutions">
    <h2 class="section-title">Solutions We Provide</h2>
    <div class="solution" style="left:123px; top:120px">
      <svg viewBox="0 0 48 48" fill="none" stroke="#1e1e1e" stroke-width="3"><path d="M12 4h18l8 8v32H12z"/><path d="M18 20h14M18 27h14M18 34h14"/><circle cx="10" cy="14" r="6" fill="#1e1e1e"/></svg>
      <div class="solution-label">Content Management</div>
    </div>
    <div class="solution" style="left:393px; top:120px">
      <svg viewBox="0 0 48 48" fill="none" stroke="#1e1e1e" stroke-width="3"><circle cx="20" cy="26" r="15"/><path d="M5 26h30M20 11v30M10 16h20M10 36h20"/><path d="M34 30l10-14" stroke-width="5"/></svg>
      <div class="solution-label">Web Design</div>
    </div>
    <div class="solution" style="left:676px; top:120px">
      <svg viewBox="0 0 48 48" fill="none" stroke="#1e1e1e" stroke-width="3"><circle cx="24" cy="24" r="19"/><path d="M16 24a8 8 0 1 0 3-6"/><path d="M15 14v6h6"/></svg>
      <div class="solution-label">Bespoke System</div>
    </div>
    <div class="solution" style="left:123px; top:228px">
      <svg viewBox="0 0 48 48" fill="none" stroke="#1e1e1e" stroke-width="3"><circle cx="22" cy="22" r="16"/><path d="M6 22h32M22 6v32M11 13h22M11 31h22"/><rect x="30" y="32" width="14" height="10" fill="#1e1e1e"/></svg>
      <div class="solution-label">e-commerce</div>
    </div>
    <div class="solution" style="left:393px; top:228px">
      <svg viewBox="0 0 48 48" fill="none" stroke="#1e1e1e" stroke-width="3"><path d="M30 12H8v30h30V22"/><path d="M16 26l6 6 20-26" stroke-width="4"/></svg>
      <div class="solution-label">Subscription System</div>
    </div>
    <div class="solution" style="left:676px; top:228px">
      <svg viewBox="0 0 48 48" fill="#1e1e1e"><rect x="8" y="20" width="32" height="6"/><rect x="8" y="29" width="32" height="6"/><rect x="8" y="38" width="32" height="6"/><path d="M6 4l10 10M42 4L32 14" stroke="#1e1e1e" stroke-width="3"/></svg>
      <div class="solution-label">Domain &amp; Hosting</div>
    </div>
  </section>

  <footer class="contact">
    <div class="contact-line primary">
      <svg width="18" height="26" viewBox="0 0 18 26"><path d="M6 1C2 3 1 8 3 14s6 10 10 11l3-5-4-3-2 2C8 17 6 12 6 9l3-1-1-6z" fill="none" stroke="#111" stroke-width="2"/></svg>
      <span>01632 960 471</span>
      <span class="gap"></span>
      <svg width="24" height="16" viewBox="0 0 24 16"><rect x="1" y="1" width="22" height="14" fill="none" stroke="#111" stroke-width="2"/><path d="M1 1l11 8 11-8" fill="none" stroke="#111" stroke-width="2"/></svg>
      <span>hello@velmoran-example.com</span>
    </div>
    <div class="contact-line address">
      <svg width="14" height="20" viewBox="0 0 14 20"><path d="M7 0a7 7 0 0 0-7 7c0 5 7 13 7 13s7-8 7-13a7 7 0 0 0-7-7z" fill="#111"/><circle cx="7" cy="7" r="2.5" fill="#fff"/></svg>
      <span>Velmoran Ltd, Brisk Suites, Quenby Road, Cheltenham, GL53 9TQ</span>
    </div>
  </footer>
</main>
</body>
</html>
```